Poster for a Bicycle show/Expo

We need a poster for a Bicycle show/Expo and sustainable transport. Exhibitors will sell bikes, cycling clothing, accessories, etc. ...
This show is annual and the Poster is for the 2015 edition.

The style must be modern, dynamic, bright colors.

Your concept must be compatible in a landscape format. (We will ourselves adaptations of different formats.)
Width: 210 mm
Height: 297 mm
It's necessary for us to have the source file (vector) for make, later, the different format (flyers, website, ...)

Content of the Poster:
- 1 big picture (no clip art)
- Big title: « Fête Roulix » (« Salon » or « Salon du » can be small and « Vélo » big.)
- Subtitle: « et de la mobilité douce »
- Date: « 8, 9 et 10 mai 2015 » or « 8-10 mai 2015 »
- Place: « Halle TRX - Quai Brenaz »
- Text line 1: « www.fete-roulix.ch - Entrée gratuite »
- Text line 2« Piste d’essais - Restauration sur place »
- Text line 3: « Ve 8 mai de 17h à 21h - Sa 9 mai de 10h à 20h - Di 10 mai de 10h à 18h »
- Please, leave a zone in the poster for sponsors logos
(The predominant information (most visible) are: « Fête Roulix » and « 8, 9 et 10 mai 2015 or 8-10 mai 2015 »)

Content of the big picture:
- from a cheap stock, like PixoBanq.com
- a bicycle in action or a detail of a bicycle (or a accessory) (no race bike)
- a modern picture with bright colors.
- if a person is on the picture, we prefer a men
- not an aerial view with cyclists in a landscape.

Some examples of poster of shows - with typo-title worked

http://www.bassinexpoville.com/Temp/IMG/F_a7c2e9b4d1f0836255e1b7a9c4d3f2e6812c9b0a4e5f7_200_296.png

http://qz4m.tolvanfoires.fr/Data/kmtolv_mer/block/F_9bd1c3e7f2a4605813c9e2d7b4a8f6c0d3e1a527f86c2.pdf
(page 2 of this PDF)

http://salons.marvelle-agenda.fr/images/marvelle-agenda/foires-salons/phototheque/expo-moto-brivanne/expo-moto-brivanne2012-affiche.jpg

http://www.drupaix.net/blog/wp-content/uploads/2007/03/affiche-foire-des-pages.jpg

http://www.voilemarine-club.com/wp-content/affiche-regate-2007.jpg

Hello,

For information, for your next versions, please, add the text "Piste d'essais".

- Text line 1: « www.fete-roulix.ch - Entrée gratuite »
- Text line 2: « Piste d’essais - Restauration sur place »
- Text line 3: « Ve 8 mai de 17h à 21h - Sa 9 mai de 10h à 20h - Di 10 mai de 10h à 18h »

Thanks,
Mathieu

Landscape

Sans Serif

```html
<!DOCTYPE html>
<html lang="fr">
<head>
<meta charset="utf-8">
<title>Fête Roulix 2015</title>
<link rel="stylesheet" href="https://fonts.googleapis.com/css2?family=Roboto:wght@300;700;900&family=Roboto+Condensed:wght@700&display=swap">
<style>
  :root {
    --paper: #ffffff;
    --orange: #f08a22;
    --pink: #ea569b;
    --ink: #111111;
    --ink-soft: #222222;
    --sky-top: #a9c8ea;
    --sky-low: #dfe8ef;
    --field: #b8a27c;
    --road: #b9b5ae;
  }
  * { margin: 0; padding: 0; box-sizing: border-box; }
  html, body { width: 848px; height: 1200px; overflow: hidden; background: var(--paper); }
  .poster {
    position: relative;
    width: 848px;
    height: 1200px;
    overflow: hidden;
    background: var(--paper);
    font-family: "Roboto", Helvetica, Arial, sans-serif;
  }
  .title {
    position: absolute;
    left: 40px;
    top: 178px;
    font-weight: 900;
    font-size: 116px;
    line-height: 1;
    letter-spacing: -1px;
    color: var(--orange);
    white-space: nowrap;
  }
  .subtitle {
    position: absolute;
    left: 42px;
    top: 326px;
    font-weight: 300;
    font-size: 49px;
    line-height: 1;
    color: var(--ink);
  }
  .band {
    position: absolute;
    left: 0;
    top: 437px;
    width: 848px;
    height: 440px;
    background: var(--pink);
  }
  .date {
    position: absolute;
    top: 468px;
    left: 0;
    width: 848px;
    text-align: center;
    font-family: "Roboto Condensed", "Arial Narrow", sans-serif;
    font-weight: 700;
    font-size: 74px;
    line-height: 1;
    color: var(--ink);
  }
  .venue {
    position: absolute;
    top: 536px;
    left: 0;
    width: 848px;
    text-align: center;
    font-weight: 300;
    font-size: 35px;
    line-height: 1;
    color: var(--ink-soft);
  }
  .photo {
    position: absolute;
    left: -100px;
    top: 588px;
    width: 600px;
    height: 600px;
  }
  .details {
    position: absolute;
    right: 36px;
    top: 660px;
    text-align: right;
    list-style: none;
    font-weight: 300;
    font-size: 20px;
    line-height: 30px;
    color: var(--ink);
  }
</style>
</head>
<body>
<main class="poster">
  <h1 class="title">Fête Roulix</h1>
  <p class="subtitle">et de la mobilité douce</p>

  <section class="band">
  </section>
  <p class="date">8, 9 et 10 mai 2015</p>
  <p class="venue">Halle TRX - Quai Brenaz</p>

  <svg class="photo" viewBox="0 0 600 600" role="img" aria-label="Photo: two cyclists riding road bikes on a sunny road, the front rider in a red jersey and white helmet on a yellow bicycle">
    <defs>
      <linearGradient id="photo-tone" x1="0" y1="0" x2="0" y2="1">
        <stop offset="0" stop-color="var(--sky-top)"/>
        <stop offset="0.48" stop-color="var(--sky-low)"/>
        <stop offset="0.62" stop-color="var(--field)"/>
        <stop offset="0.72" stop-color="var(--road)"/>
        <stop offset="1" stop-color="#d6d3ce"/>
      </linearGradient>
    </defs>
    <circle cx="300" cy="300" r="300" fill="url(#photo-tone)"/>
  </svg>

  <ul class="details">
    <li>www.fete-roulix.ch</li>
    <li>Entrée gratuite</li>
    <li>Restauration sur place</li>
    <li>Ve 8 mai de 17h à 21h</li>
    <li>Sa 9 mai de 10h à 20h</li>
    <li>Di 10 mai de 10h à 18h</li>
  </ul>
</main>
</body>
</html>
```